Multi Disciplinary Health Clinic Needs a Pop Up Banner

Vantoro Wellness needs a pop up banner ( approx. 33" x 80") to use at marketing events. We offer Chiropractic, Massage Therapy, Acupuncture, Laser Therapy, Shockwave Therapy and a lot of other modalities. We have a diverse client base ranging from children to professional athletes. More info about our clinic can be found at www.vantorowellness.ca

Target Market(s)

potential patients, all age ranges, people who are in pain or are wanting to improve their health

Industry/Entity Type

Health And Wellness

Font styles to use
Sans Serif

Requirements
Must have
• our logo
• serives: chiropractic, massage therapy, shockwave, laser
• our logo colours as the basis for the colour theme
• our website address
Nice to have
• our phone number
• images from our website ( i have high resolution files of all images)
• word font that fits with our logo font
Should not have
• an abundance of spa massage pictures. we focus more on the rehabilitation of pain and injury.

```html
<!DOCTYPE html>
<html lang="en">
<head>
<meta charset="utf-8">
<title>Vantoro Wellness – Pop Up Banner</title>
<link href="https://fonts.googleapis.com/css2?family=Questrial&family=Dancing+Script:wght@600&display=swap" rel="stylesheet">
<style>
  :root {
    --brand-blue: #1b5ea6;
    --brand-blue-light: #3a86cf;
    --brand-blue-dark: #11477f;
    --accent-grey: #6f747a;
    --text-grey: #55595e;
    --white: #ffffff;
  }
  html, body { margin: 0; padding: 0; overflow: hidden; background: var(--white); }
  .banner {
    position: relative; width: 1200px; height: 2908px; overflow: hidden;
    background: var(--white); font-family: "Questrial", sans-serif;
  }
  .brand {
    position: absolute; top: 95px; left: 0; width: 1200px;
    display: flex; align-items: center; justify-content: center; gap: 34px;
  }
  .brand-dot { width: 64px; height: 64px; border-radius: 50%; background: var(--brand-blue); }
  .brand-name { font-size: 104px; color: var(--brand-blue); font-weight: 400; letter-spacing: 1px; }
  .hero-band { position: absolute; top: 280px; left: 0; }
  .tagline {
    position: absolute; left: 0; width: 1200px; text-align: center;
    font-family: "Dancing Script", cursive; font-weight: 600; color: var(--white);
    font-size: 100px; line-height: 1;
  }
  .tagline.line-one { top: 455px; }
  .tagline.line-two { top: 600px; }
  .service-photo { position: absolute; width: 440px; height: 440px; }
  .service-name {
    position: absolute; font-size: 74px; color: var(--brand-blue); line-height: 1; white-space: nowrap;
  }
  .service-name.right-of-photo { left: 494px; }
  .service-name.left-of-photo { right: 502px; text-align: right; }
  .dotted-rule { position: absolute; height: 0; border-top: 4px dotted var(--brand-blue); }
  .rule-right { left: 494px; width: 706px; }
  .rule-left { left: 0; width: 698px; }
  .other-title {
    position: absolute; top: 2352px; left: 0; width: 1200px; text-align: center;
    font-size: 46px; color: var(--text-grey);
  }
  .other-rule { position: absolute; left: 52px; width: 1096px; border-top: 4px dotted var(--text-grey); }
  .other-item { position: absolute; font-size: 44px; color: var(--text-grey); white-space: nowrap; }
  .divider-bar { position: absolute; top: 2619px; left: 0; width: 1200px; height: 20px; background: var(--accent-grey); }
  .footer { position: absolute; top: 2648px; left: 0; width: 1200px; height: 260px; background: var(--brand-blue); }
  .call-label { position: absolute; top: 2726px; left: 172px; font-size: 42px; color: var(--white); }
  .phone { position: absolute; top: 2678px; left: 322px; font-size: 100px; color: var(--white); line-height: 1; }
  .web-tab { position: absolute; top: 2786px; left: 0; }
  .website {
    position: absolute; top: 2808px; left: 0; width: 1200px; text-align: center;
    font-size: 52px; color: var(--brand-blue); letter-spacing: 2px;
  }
</style>
</head>
<body>
<main class="banner">

  <header class="brand">
    <span class="brand-dot"></span>
    <span class="brand-name">Vantoro Wellness</span>
  </header>

  <svg class="hero-band" width="1200" height="540" viewBox="0 0 1200 540" aria-hidden="true">
    <defs>
      <linearGradient id="bandFill" x1="0" y1="0" x2="1" y2="0">
        <stop offset="0" stop-color="#11477f"/>
        <stop offset="0.5" stop-color="#3a86cf"/>
        <stop offset="1" stop-color="#11477f"/>
      </linearGradient>
    </defs>
    <path d="M0 10 Q600 260 1200 10 L1200 355 Q600 680 0 355 Z" fill="#6f747a" opacity="0.55"/>
    <path d="M0 10 Q600 260 1200 10 L1200 340 Q600 640 0 340 Z" fill="url(#bandFill)"/>
  </svg>
  <div class="tagline line-one">helping you live life</div>
  <div class="tagline line-two">pain free</div>

  <!-- Chiropractic -->
  <svg class="service-photo" style="left:32px; top:768px;" viewBox="0 0 440 440" role="img" aria-label="Photo of a chiropractor gently adjusting a baby">
    <circle cx="208" cy="208" r="202" fill="#6f747a"/>
    <circle cx="220" cy="220" r="200" fill="#ffffff"/>
    <defs><radialGradient id="photoChiro"><stop offset="0" stop-color="#e9ddd0"/><stop offset="1" stop-color="#2e4a66"/></radialGradient></defs>
    <circle cx="220" cy="220" r="190" fill="url(#photoChiro)"/>
  </svg>
  <div class="service-name right-of-photo" style="top:950px;">Chiropractic</div>
  <div class="dotted-rule rule-right" style="top:1031px;"></div>

  <!-- Acupuncture -->
  <svg class="service-photo" style="left:720px; top:1054px;" viewBox="0 0 440 440" role="img" aria-label="Photo of a woman relaxing during acupuncture treatment">
    <circle cx="232" cy="208" r="202" fill="#6f747a"/>
    <circle cx="220" cy="220" r="200" fill="#ffffff"/>
    <defs><radialGradient id="photoAcu"><stop offset="0" stop-color="#f3dccb"/><stop offset="1" stop-color="#e8e8ea"/></radialGradient></defs>
    <circle cx="220" cy="220" r="190" fill="url(#photoAcu)"/>
  </svg>
  <div class="service-name left-of-photo" style="top:1236px;">Acupuncture</div>
  <div class="dotted-rule rule-left" style="top:1322px;"></div>

  <!-- Massage Therapy -->
  <svg class="service-photo" style="left:32px; top:1343px;" viewBox="0 0 440 440" role="img" aria-label="Photo of a therapist massaging a patient's knee">
    <circle cx="208" cy="208" r="202" fill="#6f747a"/>
    <circle cx="220" cy="220" r="200" fill="#ffffff"/>
    <defs><radialGradient id="photoMassage"><stop offset="0" stop-color="#e6cdb8"/><stop offset="1" stop-color="#2c2f3a"/></radialGradient></defs>
    <circle cx="220" cy="220" r="190" fill="url(#photoMassage)"/>
  </svg>
  <div class="service-name right-of-photo" style="top:1525px;">Massage Therapy</div>
  <div class="dotted-rule rule-right" style="top:1605px;"></div>

  <!-- Laser Therapy -->
  <svg class="service-photo" style="left:720px; top:1652px;" viewBox="0 0 440 440" role="img" aria-label="Photo of a hand applying a laser therapy probe">
    <circle cx="232" cy="208" r="202" fill="#6f747a"/>
    <circle cx="220" cy="220" r="200" fill="#ffffff"/>
    <defs><radialGradient id="photoLaser"><stop offset="0" stop-color="#a86a4a"/><stop offset="1" stop-color="#2b3a52"/></radialGradient></defs>
    <circle cx="220" cy="220" r="190" fill="url(#photoLaser)"/>
  </svg>
  <div class="service-name left-of-photo" style="top:1828px;">Laser Therapy</div>
  <div class="dotted-rule rule-left" style="top:1914px;"></div>

  <!-- Shockwave Therapy -->
  <svg class="service-photo" style="left:32px; top:1942px;" viewBox="0 0 440 440" role="img" aria-label="Photo of a shockwave device applied to the sole of a foot">
    <circle cx="208" cy="208" r="202" fill="#6f747a"/>
    <circle cx="220" cy="220" r="200" fill="#ffffff"/>
    <defs><radialGradient id="photoShock"><stop offset="0" stop-color="#e9cdb6"/><stop offset="1" stop-color="#d9d9dc"/></radialGradient></defs>
    <circle cx="220" cy="220" r="190" fill="url(#photoShock)"/>
  </svg>
  <div class="service-name right-of-photo" style="top:2122px;">Shockwave Therapy</div>
  <div class="dotted-rule rule-right" style="top:2204px;"></div>

  <!-- Other services -->
  <div class="other-title">Other Services</div>
  <div class="other-rule" style="top:2409px;"></div>
  <div class="other-item" style="left:52px; top:2430px;">Active Glide Technique</div>
  <div class="other-item" style="left:664px; top:2430px;">|</div>
  <div class="other-item" style="left:716px; top:2430px;">Stratus Technique</div>
  <div class="other-item" style="left:52px; top:2511px;">Cupping Technique</div>
  <div class="other-item" style="left:664px; top:2511px;">|</div>
  <div class="other-item" style="left:716px; top:2511px;">Kinesiology Taping</div>
  <div class="other-rule" style="top:2596px;"></div>

  <!-- Footer -->
  <div class="divider-bar"></div>
  <footer class="footer"></footer>
  <div class="call-label">Call us:</div>
  <div class="phone">(403) 555 0182</div>
  <svg class="web-tab" width="1200" height="122" viewBox="0 0 1200 122" aria-hidden="true">
    <path d="M222 122 C262 122 250 0 330 0 L870 0 C950 0 938 122 978 122 Z" fill="#ffffff"/>
  </svg>
  <div class="website">www.vantorowellness.ca</div>

</main>
</body>
</html>
```